WordPress Design (redesign) and Coding for Funeral Consulting Services & mobile app

I need an attractive SEO friendly WordPress design.

Incorporating all of the latest design standards in a graceful and appealing way. I'd like to see CTA's for for funeral consulting services. People should be able to purchase my consulting services directly from the website so I'd like to see nice buttons.

Funeral Consulting Services are the main topic for this website.

I also have an iOS app called Velmoreth in the Zentrova Market. I want buttons and CTAs so that users can download the app right to their iOS device(s). Make this a secondary focus.

I want more of a mobile focus as that is where I expect the most traffic. Mobile users like to act quickly and they also like to scroll if their interest is captured so I want the design to reflect that.

End to end design
Large Creative Typography for increased mobile searchers.
attractive CTA’s
RGB Vivid / Bright Colors that match our logo
A menu that is easy to find and use on mobile devices
button(s) for iOS app download.

the current website is www.velmoreth.example This website was a placeholder.
Updates

I'd need users to fill out a survey so that I may collect information from them to better provide service to them.

reference websites: Quorbantix.example & Plinder.example for website design inspiratioin. reference Marsvenko.example for blog

Target Market(s)

18-35 year old mobile users

Industry/Entity Type

Consulting

Coding

Coded - Design and coding required

Font styles to use
Sans Serif

Colors
fbee3d
000000
ffffff
cbcbcb
fefdec

Requirements
Must have
• iOS app logo and iOS app logo colors should have its own area/page
• CTA's for consulting services and app download. Main topic
• reviews (testimonials)
• Video area
• end to end design
• creative typography
Nice to have
• a beautiful blog page that blends well with the design
Should not have
• Any imagery related to funerals or burials.

```html
<!DOCTYPE html>
<html lang="en">
<head>
<meta charset="utf-8">
<title>Velmoreth – Funeral Consulting</title>
<link href="https://fonts.googleapis.com/css2?family=Montserrat:wght@400;600;700;800&family=Roboto:wght@300;400;500;700&display=swap" rel="stylesheet">
<style>
:root{
  --yellow:#fbee3d;
  --gold:#f5c400;
  --black:#000000;
  --ink:#1b1b1b;
  --dark:#2a2a2a;
  --white:#ffffff;
  --grey:#cbcbcb;
  --muted:#7a7a7a;
  --cream:#fefdec;
  --footer:#161616;
  --head:'Montserrat',sans-serif;
  --body:'Roboto',sans-serif;
}
*{box-sizing:border-box;margin:0;padding:0}
html,body{width:1200px;height:3766px;overflow:hidden;background:var(--white);font-family:var(--body);color:var(--ink)}
.page{position:relative;width:1200px;height:3766px;overflow:hidden}
.abs{position:absolute}
.btn{display:inline-block;border-radius:20px;background:var(--yellow);color:var(--black);font:600 12px var(--body);padding:11px 26px}
.store{display:inline-flex;align-items:center;gap:8px;border:2px solid var(--white);border-radius:10px;background:var(--black);color:var(--white);padding:6px 14px;font:500 13px var(--body)}
.store small{display:block;font-size:8px;opacity:.8}
.store i{width:16px;height:16px;border-radius:50%;background:var(--white);display:block}
.photo{position:absolute}

/* hero */
.hero{position:absolute;left:0;top:0;width:1200px;height:535px}
.hero-shade{position:absolute;inset:0;background:linear-gradient(180deg,rgba(0,0,0,.1),rgba(0,0,0,.55))}
.hero h1{position:absolute;top:300px;width:100%;text-align:center;font:800 44px var(--head);color:var(--white);letter-spacing:1px}
.hero p{position:absolute;top:356px;width:100%;text-align:center;font:400 16px var(--body);color:var(--white)}
.hero .ctas{position:absolute;top:400px;width:100%;display:flex;justify-content:center;gap:18px;align-items:center}
.hero-dot{position:absolute;left:-40px;top:300px;width:100px;height:100px;border-radius:50%;background:var(--yellow)}

/* nav */
.nav{position:absolute;top:535px;left:0;width:1200px;height:48px;background:var(--black)}
.nav ul{list-style:none;position:absolute;top:16px;display:flex;gap:24px;font:500 12px var(--body);color:var(--white)}
.nav .left{left:250px}
.nav .right{left:745px}
.nav .store{position:absolute;left:958px;top:8px;padding:3px 10px;font-size:11px;border-width:1px}
.logo-ring{position:absolute;left:525px;top:485px;width:150px;height:150px;border-radius:50%;background:var(--black);border:6px solid var(--yellow);display:flex;align-items:center;justify-content:center}
.logo-ring span{width:96px;height:96px;border-radius:50%;background:var(--white);display:flex;align-items:center;justify-content:center;font:700 15px var(--head);color:var(--black)}
.brand{position:absolute;top:655px;width:100%;text-align:center;font:700 22px var(--head);color:var(--black)}

/* about */
.ring{position:absolute;border-radius:50%;border-style:solid;border-color:var(--gold)}
.about h2{position:absolute;left:250px;top:812px;font:800 30px var(--head);color:var(--black)}
.about .lead{position:absolute;left:250px;top:855px;width:380px;font:300 19px/1.3 var(--body)}
.about .copy{position:absolute;left:250px;top:918px;width:390px;font:400 10px/1.6 var(--body);color:var(--muted)}
.about .btn{position:absolute;left:250px;top:1002px}
.about-frame{position:absolute;left:668px;top:790px;width:305px;height:335px;border:2px solid var(--gold)}

/* mission band */
.band-shape{position:absolute;left:0;top:1150px}
.band-text{position:absolute;left:250px;top:1275px;width:700px;text-align:center;font:300 16px/1.6 var(--body);color:var(--white)}
.band-btn{position:absolute;left:522px;top:1368px}

/* services */
.title{position:absolute;width:100%;text-align:center;font:800 30px var(--head);color:var(--black)}
.sub{position:absolute;left:380px;width:440px;text-align:center;font:400 10px/1.6 var(--body);color:var(--grey)}
.service{position:absolute;top:1625px;width:220px;text-align:center}
.service .disc{margin:0 auto;width:150px;height:150px;border-radius:50%;border:1px solid #e2e2e2;display:flex;align-items:center;justify-content:center;background:var(--white)}
.service .core{width:108px;height:108px;border-radius:50%;background:radial-gradient(circle at 40% 35%,var(--yellow),var(--gold));display:flex;align-items:center;justify-content:center}
.service h3{margin-top:26px;font:700 13px var(--head)}
.service p{margin-top:8px;font:400 10px/1.5 var(--body);color:var(--muted)}

/* blog */
.card{position:absolute;background:var(--white);padding:24px 22px}
.card .meta{font:500 9px var(--body);color:var(--muted)}
.card h4{margin-top:8px;font:800 16px/1.2 var(--head);color:var(--black)}
.card p{margin-top:10px;font:400 9px/1.6 var(--body);color:var(--muted)}
.card.big h4{font-size:24px}
.card.big p{font-size:10px}
.card.framed{border:8px solid var(--gold)}

/* testimonials */
.avatar{position:absolute;border-radius:50%;background:linear-gradient(160deg,#c9c2b8,#8e8780)}
.arrow{position:absolute;width:30px;height:30px;border-radius:50%;background:var(--yellow);display:flex;align-items:center;justify-content:center}
.name{position:absolute;top:3150px;width:100%;text-align:center;font:700 14px var(--head)}
.role{position:absolute;top:3172px;width:100%;text-align:center;font:400 10px var(--body);color:var(--muted)}

/* contact strip */
.strip{position:absolute;left:238px;top:3276px;width:723px;height:90px;background:var(--gold);border-radius:6px;display:flex;align-items:center;justify-content:space-around;padding:0 20px;z-index:2}
.strip .item{display:flex;align-items:center;gap:14px;font:400 10px/1.6 var(--body);color:var(--black)}

/* footer */
.footer-bg{position:absolute;left:0;top:3313px;width:1200px;height:453px;background:var(--footer)}
.foot-head{position:absolute;top:3408px;font:800 15px var(--head);color:var(--white)}
.foot-list{position:absolute;top:3448px;list-style:none;font:400 10px/2.3 var(--body);color:#bdbdbd}
.foot-list li::before{content:"";display:inline-block;width:4px;height:4px;background:var(--gold);border-radius:50%;margin-right:8px;vertical-align:middle}
.ftxt{position:absolute;font:400 10px/1.6 var(--body);color:#bdbdbd}
.foot-label{position:absolute;top:3667px;font:800 10px var(--head);color:var(--white);white-space:nowrap}
.social{position:absolute;top:3658px;left:425px;display:flex;gap:6px}
.social span{width:26px;height:26px;background:var(--gold)}
.news{position:absolute;left:728px;top:3658px;width:250px;height:28px;display:flex}
.news div{flex:1;background:var(--white);font:400 10px var(--body);color:var(--muted);padding:8px 10px}
.news b{width:60px;background:var(--gold);color:var(--black);font:700 10px var(--body);display:flex;align-items:center;justify-content:center}
.copyright{position:absolute;left:0;top:3720px;width:1200px;height:46px;border-top:1px solid #333;font:400 10px var(--body);color:#bdbdbd;padding:14px 250px}
</style>
</head>
<body>
<div class="page">

  <!-- hero -->
  <section class="hero">
    <div class="photo" role="img" aria-label="Team of consultants working together at laptops" style="inset:0;background:linear-gradient(120deg,#44576b,#6f7f90 45%,#3a4552)"></div>
    <div class="hero-shade"></div>
    <div class="hero-dot"></div>
    <h1>FUNERALS ARE EXPENSIVE</h1>
    <p>Having to finance one suddenly can be a burden to many families, especially those</p>
    <div class="ctas">
      <span class="btn">DON'T Throw Money Away</span>
      <span class="store"><i></i><span><small>Download on the</small>Zentrova Market</span></span>
    </div>
  </section>

  <nav class="nav">
    <ul class="left"><li>Home</li><li>About us</li><li>Services</li><li>Team</li></ul>
    <ul class="right"><li>Testimonials</li><li>Blog</li><li>Contact us</li></ul>
    <span class="store"><i></i>Zentrova Market</span>
  </nav>
  <div class="logo-ring"><span>Velmoreth</span></div>
  <div class="brand">Velmoreth</div>

  <!-- about -->
  <section class="about">
    <div class="ring" style="left:-190px;top:765px;width:330px;height:330px;border-width:48px"></div>
    <h2>ABOUT US</h2>
    <p class="lead">The first step in funeral pl&amp;nning, particularly if you find yourself at-need</p>
    <p class="copy">It is good to plan ahead with someone you trust. A consultant works beside the family, takes on the hard tasks, and keeps each decision clear and calm. We compare providers, explain every cost and help you avoid the pressure that leads to expensive choices. Our aim is to keep the whole process within reach for every family we serve, so nobody feels lost at a hard time.</p>
    <span class="btn">Save Money Today</span>
    <div class="about-frame"></div>
    <div class="photo" role="img" aria-label="Consultants in headsets at an office desk" style="left:672px;top:715px;width:528px;height:355px;background:linear-gradient(135deg,#e9edf1,#a9b3bd 60%,#6d7885)"></div>
  </section>

  <!-- mission band -->
  <svg class="band-shape" width="1200" height="370" viewBox="0 0 1200 370">
    <polygon points="0,0 1200,110 1200,370 0,250" fill="#262626"/>
    <polygon points="0,0 1200,110 1200,130 0,20" fill="#3a3a3a"/>
  </svg>
  <p class="band-text">A funeral consultant is someone who, on their own, goes out and does all the things related to making funeral arrangements. However we do so with your budget and your ideals in mind. We represent you as your spokesperson and friend during this tough time.</p>
  <span class="btn band-btn">Get Help ASAP</span>

  <!-- services -->
  <section>
    <div class="photo" role="img" aria-label="Faded portrait of a businessman" style="left:900px;top:1500px;width:300px;height:410px;background:linear-gradient(180deg,#f4f4f4,#e4e4e4)"></div>
    <h2 class="title" style="top:1505px">OUR SERVICES</h2>
    <p class="sub" style="top:1548px">Lorem ipsum is simply dummy text of the printing and typesetting industry. Lorem Ipsum has been the industry's standard dummy text ever since the 1500s</p>
    <div class="service" style="left:234px">
      <div class="disc"><div class="core">
        <svg width="44" height="44" viewBox="0 0 44 44" fill="none" stroke="#000" stroke-width="2.4"><circle cx="22" cy="17" r="8"/><path d="M8 38c2-9 26-9 28 0"/><path d="M12 18a10 10 0 0 1 20 0"/></svg>
      </div></div>
      <h3>FINANCIAL CONSULTANT</h3>
      <p>Lorem ipsum is simply dummy text of the printing and typesetting industry.</p>
    </div>
    <div class="service" style="left:505px">
      <div class="disc"><div class="core">
        <svg width="44" height="44" viewBox="0 0 44 44" fill="none" stroke="#000" stroke-width="2.4"><path d="M6 38h32"/><rect x="9" y="26" width="5" height="12"/><rect x="19" y="20" width="5" height="18"/><rect x="29" y="14" width="5" height="24"/><path d="M8 20l10-8 8 5 12-10"/></svg>
      </div></div>
      <h3>BEST CONSULTING</h3>
      <p>Lorem ipsum is simply dummy text of the printing and typesetting industry.</p>
    </div>
    <div class="service" style="left:761px">
      <div class="disc"><div class="core">
        <svg width="44" height="44" viewBox="0 0 44 44" fill="none" stroke="#000" stroke-width="2.4"><path d="M14 38v-8c-5-3-7-8-6-13 2-8 10-11 17-9 7 2 11 9 9 16-1 3-3 5-5 6v8"/><circle cx="22" cy="19" r="4"/></svg>
      </div></div>
      <h3>SUCCESSFUL PLANNER</h3>
      <p>Lorem ipsum is simply dummy text of the printing and typesetting industry.</p>
    </div>
  </section>

  <!-- blog -->
  <section>
    <div class="abs" style="left:0;top:1908px;width:1200px;height:865px;background:#f3f3f3"></div>
    <h2 class="title" style="top:1940px">LATEST BLOG</h2>

    <div class="photo" role="img" aria-label="Business people shaking hands" style="left:0;top:2008px;width:301px;height:213px;background:linear-gradient(135deg,#dfe5ea,#8b98a6)"></div>
    <div class="card" style="left:301px;top:2020px;width:289px;height:190px">
      <div class="meta">MY ADMIN &nbsp;|&nbsp; 28 Dec 2017</div>
      <h4>LOREM IPSUM IS SIMPLY DUMMY TEXT OF THE PRINTING</h4>
      <p>Lorem Ipsum is simply dummy text of the printing and typesetting industry. Lorem Ipsum has been the standard dummy text ever since the 1500s.</p>
    </div>
    <div class="photo" role="img" aria-label="Man working on a desktop computer" style="left:602px;top:2008px;width:297px;height:213px;background:linear-gradient(135deg,#eef1f3,#9aa4ae)"></div>
    <div class="card" style="left:899px;top:2020px;width:290px;height:190px">
      <div class="meta">MY ADMIN &nbsp;|&nbsp; 28 Dec 2017</div>
      <h4>LOREM IPSUM IS SIMPLY DUMMY TEXT OF THE PRINTING</h4>
      <p>Lorem Ipsum is simply dummy text of the printing and typesetting industry. Lorem Ipsum has been the standard dummy text ever since the 1500s.</p>
    </div>

    <div class="photo" role="img" aria-label="Team reviewing charts around a table" style="left:0;top:2221px;width:602px;height:327px;background:linear-gradient(135deg,#5b5f66,#b9a98f 50%,#3f434a)"></div>
    <div class="card big" style="left:602px;top:2221px;width:598px;height:327px;padding:60px 40px">
      <div class="meta">MY ADMIN &nbsp;|&nbsp; 28 Dec 2017</div>
      <h4>LOREM IPSUM IS SIMPLY<br>DUMMY TEXT OF THE PRINTING</h4>
      <p>Lorem Ipsum is simply dummy text of the printing and typesetting industry. Lorem Ipsum has been the industry's standard dummy text ever since the 1500s, when an unknown printer took a galley of type and scrambled it to make a type specimen book.</p>
      <p>It has survived not only five centuries, but also the leap into electronic typesetting, remaining essentially unchanged. It was popularised in the 1960s with the release of sheets containing passages.</p>
    </div>

    <div class="photo" role="img" aria-label="Colleagues talking in a meeting" style="left:0;top:2548px;width:301px;height:213px;background:linear-gradient(135deg,#c8c2b6,#7b7468)"></div>
    <div class="card framed" style="left:301px;top:2548px;width:294px;height:213px">
      <div class="meta">MY ADMIN &nbsp;|&nbsp; 28 Dec 2017</div>
      <h4>LOREM IPSUM IS SIMPLY DUMMY TEXT OF THE PRINTING</h4>
      <p>Lorem Ipsum is simply dummy text of the printing and typesetting industry. Lorem Ipsum has been the standard dummy text ever since the 1500s.</p>
    </div>
    <div class="photo" role="img" aria-label="Team working at laptops in a bright office" style="left:602px;top:2548px;width:297px;height:213px;background:linear-gradient(135deg,#e7e9ea,#9aa2a6)"></div>
    <div class="card" style="left:899px;top:2560px;width:290px;height:190px">
      <div class="meta">MY ADMIN &nbsp;|&nbsp; 28 Dec 2017</div>
      <h4>LOREM IPSUM IS SIMPLY DUMMY TEXT OF THE PRINTING</h4>
      <p>Lorem Ipsum is simply dummy text of the printing and typesetting industry. Lorem Ipsum has been the standard dummy text ever since the 1500s.</p>
    </div>
  </section>

  <!-- testimonials -->
  <section>
    <div class="photo" role="img" aria-label="Faded portrait of a man in glasses" style="left:0;top:2773px;width:520px;height:540px;background:linear-gradient(90deg,#e6e6e6,#f7f7f7)"></div>
    <div class="ring" style="left:1080px;top:2880px;width:300px;height:300px;border-width:48px"></div>
    <h2 class="title" style="top:2810px">TESTIMONIALS</h2>
    <p class="sub" style="top:2858px;left:330px;width:540px;color:var(--muted)">Lorem Ipsum is simply dummy text of the printing and typesetting industry. Lorem Ipsum has been the industry's standard dummy text ever since the 1500s, when an unknown printer took a galley of type and scrambled it to make a type specimen book.</p>
    <svg class="abs" style="left:240px;top:3035px" width="720" height="2"><line x1="0" y1="1" x2="720" y2="1" stroke="#cbcbcb"/></svg>
    <div class="arrow" style="left:216px;top:3020px"><svg width="10" height="12"><path d="M8 1L2 6l6 5" fill="none" stroke="#000" stroke-width="2"/></svg></div>
    <div class="arrow" style="left:952px;top:3020px"><svg width="10" height="12"><path d="M2 1l6 5-6 5" fill="none" stroke="#000" stroke-width="2"/></svg></div>
    <div class="avatar" role="img" aria-label="Client portrait" style="left:290px;top:2996px;width:80px;height:80px;border:4px solid #ddd"></div>
    <div class="avatar" role="img" aria-label="Client portrait" style="left:832px;top:2996px;width:80px;height:80px;border:4px solid #ddd"></div>
    <div class="abs" style="left:492px;top:2928px;width:216px;height:216px;border-radius:50%;background:var(--gold)"></div>
    <div class="avatar" role="img" aria-label="Client portrait" style="left:508px;top:2944px;width:184px;height:184px;background:linear-gradient(160deg,#ede9e4,#b8b0a6)"></div>
    <div class="name">ORIN VASTEL</div>
    <div class="role">IIT Dev Team</div>
  </section>

  <!-- footer -->
  <footer>
    <div class="footer-bg"></div>
    <div class="strip">
      <div class="item">
        <svg width="30" height="38" viewBox="0 0 30 38" fill="none" stroke="#000" stroke-width="2"><rect x="5" y="2" width="20" height="34" rx="3"/><line x1="12" y1="31" x2="18" y2="31"/></svg>
        <span>Phone: 000 0000 0000<br>Fax: 000 0000 0000</span>
      </div>
      <div class="item">
        <svg width="38" height="30" viewBox="0 0 38 30" fill="none" stroke="#000" stroke-width="2"><rect x="2" y="3" width="34" height="24"/><path d="M2 3l17 14L36 3"/></svg>
        <span>Email: info@velmoreth.example<br>Email: contact@velmoreth.example</span>
      </div>
      <div class="item">
        <svg width="28" height="38" viewBox="0 0 28 38" fill="none" stroke="#000" stroke-width="2"><path d="M14 36S3 22 3 13a11 11 0 0 1 22 0c0 9-11 23-11 23z"/><circle cx="14" cy="13" r="4"/></svg>
        <span>Address: Lorem ipsum is simply dummy text<br>of the printing and typesetting industry.</span>
      </div>
    </div>

    <div class="abs" style="left:250px;top:3398px;width:56px;height:56px;border-radius:50%;background:var(--black);border:3px solid var(--gold);display:flex;align-items:center;justify-content:center;font:700 8px var(--head);color:var(--white)">Velmoreth</div>
    <p class="ftxt" style="left:250px;top:3470px;width:230px">It is good to plan with a friend you trust. This should be someone who is calm and kind and can guide the family.</p>
    <p class="ftxt" style="left:250px;top:3540px;width:230px">Address: Lorem ipsum is simply dummy text of the printing and typesetting industry.<br><br>Phone Number: 000 0000 0000<br><br>Email: info@velmoreth.example</p>

    <h5 class="foot-head" style="left:515px">LINKS</h5>
    <ul class="foot-list" style="left:515px"><li>Home</li><li>About us</li><li>Services</li><li>Testimonials</li><li>Blog</li><li>Contact us</li></ul>

    <h5 class="foot-head" style="left:622px">SERVICES</h5>
    <ul class="foot-list" style="left:622px"><li>Best Consulting</li><li>Successful Planner</li><li>Financial Consulting</li><li>Funeral consulting</li><li>Business Consulting</li></ul>

    <h5 class="foot-head" style="left:753px">TWEETS</h5>
    <p class="ftxt" style="left:753px;top:3448px;width:200px">@Velmoreth Lorem ipsum is simply dummy text of the printing industry.<br>14 Dec 2017</p>
    <p class="ftxt" style="left:753px;top:3510px;width:200px">@Velmoreth Lorem ipsum is simply dummy text of the printing industry.<br>14 Dec 2017</p>
    <span class="store abs" style="left:753px;top:3565px;padding:3px 10px;font-size:11px;border-width:1px"><i></i>Zentrova Market</span>

    <div class="foot-label" style="left:250px">FOLLOW US ON SOCIAL MEDIA</div>
    <div class="social"><span></span><span></span><span></span><span></span><span></span><span></span></div>
    <div class="foot-label" style="left:645px">NEWSLETTER</div>
    <div class="news"><div>Your Email Address</div><b>SEND</b></div>

    <div class="copyright">Copyright © 2017 <b style="color:var(--white)">Velmoreth</b>. All Rights Reserved.</div>
  </footer>

</div>
</body>
</html>
```